Bright Path Flyer Design for Virtual Online Clinic. -5.5 x 8.5 inches (half sheet)

We need a clean, modern flyer design for Bright Path, a new virtual walk-in clinic based in British Columbia. The flyer will be used in libraries, pharmacies, and community centers to help residents easily access primary care through their Bright Path NFC access card.
The flyer will ask a question : NEED A DOCTOR? This should be large and attention grabbing.
The design should clearly feature a Bright Path card image (the access card) as the centerpiece and visually show how patients can use it to book appointments. The tone should feel trustworthy, healthcare-oriented, and community-friendly — clean fonts, clear spacing, and strong readability from a distance.

Side One: This card has the NFC Access Card.
NEED A DOCTOR? (Large Font, Attention Grabbing)
How to Book an Appointment using your Bright Path Card
Step 1: Tap Your Card on Your Phone
Hold your card near the back of your phone.
It will activate automatically — no app needed.
The Bright Path scheduler will open.
Step 2: Schedule Your Appointment
Select your clinical concern.
Choose your time window.
Register (only once).
Confirm your appointment.
Step 3: Relax, we’ll take care of the rest
A doctor will call during your scheduled time.
Once booked, you’ll be able to call our office.
No emails, no texts — just a real person.
It’s that simple.
Side Two:
About Bright Path
Created by Dr. Marcus Ferrigan
Bright Path was founded to make healthcare simple and convenient. Prescription renewals. Common infections. Medical notes. And so much more.
Our doctors can address 120+ health concerns virtually — providing quality care without the waiting room. No waiting rooms. Just real doctors providing real care.
Why Patients Choose Bright Path
Easy access – book and be seen from anywhere in BC.
Effortless booking – tap your Bright Path Card to begin.
Trusted physicians – every visit is with a licensed BC family doctor.
How It Works
Book your visit — choose a time window that fits your day.
Join the queue — you’ll be called when it’s your turn.
Speak directly with your doctor — simple, secure, and stress-free.
Convenient Care for Common Concerns

Additional Details.
Please find the domain to be launched soon. I've attached the NFC card file for review, it is 85.5 mm x 54 mm. The card will be glued to the flyer.
I've attached examples of flyers but they are not the look I am seeking and I am looking for creative solutions.
Thank you!
http://brightpath-example.test/

Adult Patients in British Columbia

Healthcare

• Looking for clean lines, uniform appearance, and high legibility i.e poppins

0054AA
0677BA
7BADD7
CADEEF
E8F1F8

• Need A Doctor?
• Elegant style, not too busy, clear layout.
• Clutter, look cheap - review examples.

```html
<!DOCTYPE html>
<html lang="en">
<head>
<meta charset="utf-8">
<title>Bright Path Flyer</title>
<link href="https://fonts.googleapis.com/css2?family=Poppins:wght@300;400;500;600;700;800&display=swap" rel="stylesheet">
<style>
:root{
  --navy:#2a4490;
  --brand-blue:#2a4fb5;
  --sky:#d4edfb;
  --cyan:#1aa6e0;
  --backdrop:#3bb5e8;
  --ink:#1d2233;
  --white:#ffffff;
}
*{box-sizing:border-box;margin:0;padding:0}
html,body{width:1200px;height:1200px;overflow:hidden}
body{background:var(--backdrop);font-family:'Poppins',sans-serif;color:var(--ink);position:relative}
.sheet{position:absolute;top:206px;width:486px;height:750px;background:var(--white);overflow:hidden}
.sheet--front{left:100px}
.sheet--back{left:625px}
.abs{position:absolute}

/* front */
.top-band{left:48px;top:0;width:390px;height:186px;background:var(--sky);border-radius:0 0 30px 30px}
.access-card{left:96px;top:48px;width:298px;height:187px;background:var(--navy);border-radius:12px;color:var(--white);text-align:center}
.access-card .brand{position:absolute;left:0;right:0;top:68px;font-size:26px;font-weight:500;display:flex;justify-content:center;align-items:center;gap:8px}
.brand-dot{width:14px;height:14px;border-radius:50%;background:var(--white);display:inline-block}
.access-card .url{position:absolute;left:0;right:0;top:112px;font-size:9.5px;letter-spacing:.5px}
.headline{left:0;right:0;top:256px;text-align:center;font-size:46px;font-weight:800;color:var(--navy);letter-spacing:-.5px;line-height:60px}
.lead{left:98px;width:290px;top:324px;text-align:center;font-size:11.3px;line-height:17px}
.steps-panel{left:48px;top:414px;width:390px;height:306px;background:var(--sky);border-radius:30px}
.book-pill{left:109px;top:390px;width:268px;height:58px;background:var(--navy);color:var(--white);border-radius:30px;text-align:center;font-size:14.5px;font-weight:500;line-height:19px;padding-top:10px}
.tap-illustration{left:0;top:490px;width:124px;height:230px;background:linear-gradient(160deg,#e9c7a8,#2a4490 60%,#e2b895);border-radius:10px 20px 0 0}
.step{left:136px;width:300px}
.step h3{font-size:11px;font-weight:600;color:var(--brand-blue);display:flex;align-items:center;gap:6px;margin-bottom:1px;line-height:16px}
.radio{width:11px;height:11px;border-radius:50%;border:1.5px solid var(--cyan);display:inline-flex;align-items:center;justify-content:center;flex:none}
.radio::after{content:"";width:5px;height:5px;border-radius:50%;background:var(--cyan)}
.step ul{list-style:none;padding-left:17px;font-size:10px;line-height:14.7px}
.step li::before{content:"• "}

/* back */
.masthead{left:22px;top:0;width:441px;height:103px;background:var(--navy);border-radius:0 0 14px 14px;color:var(--white);display:flex;align-items:center;justify-content:center;gap:10px;font-size:30px;font-weight:500}
.masthead .brand-dot{width:16px;height:16px}
.panel{background:var(--sky);border-radius:14px}
.label{background:var(--navy);color:var(--white);border-radius:8px;font-weight:600;text-align:center;font-size:14px;line-height:26px}
.about{left:22px;top:128px;width:214px;height:300px}
.services{left:249px;top:128px;width:214px;height:300px}
.about-copy{left:30px;top:147px;width:200px;font-size:9.4px;line-height:14.7px;letter-spacing:-.2px}
.about-copy p{margin-bottom:8px}
.about-copy strong{font-weight:600;color:#000}
.services-copy{left:266px;top:147px;width:190px;font-size:9.4px;line-height:14.7px}
.service-list{left:261px;top:205px;width:189px;height:176px;background:var(--white);border-radius:10px;padding:14px 12px 0 14px;font-size:9.4px;line-height:14.7px;color:var(--brand-blue);letter-spacing:-.2px}
.why{left:22px;top:447px;width:441px;height:87px}
.why-item{top:481px}
.why-item h4{font-size:11.5px;font-weight:600;color:var(--brand-blue);display:flex;align-items:center;gap:6px;white-space:nowrap}
.why-item .radio{border-color:var(--navy);width:13px;height:13px}
.why-item .radio::after{background:var(--navy);width:7px;height:7px}
.why-item p{padding-left:19px;font-size:9.8px;line-height:15px}
.visit{left:22px;top:556px;width:441px;height:134px}
.visit-step{top:583px;width:92px}
.num{width:20px;height:20px;border-radius:50%;background:var(--cyan);color:var(--white);font-size:12px;font-weight:600;display:flex;align-items:center;justify-content:center;margin-bottom:3px}
.visit-step h4{font-size:9.8px;font-weight:600;color:var(--brand-blue);line-height:12px;margin-bottom:6px;white-space:nowrap}
.visit-step p{font-size:5.8px;line-height:9.8px}
.footer-band{left:22px;top:704px;width:441px;height:46px;background:var(--navy);border-radius:14px 14px 0 0;color:var(--white);text-align:center;font-size:14px;font-weight:300;line-height:46px}
</style>
</head>
<body>

<section class="sheet sheet--front">
  <div class="abs top-band"></div>
  <div class="abs access-card">
    <div class="brand"><span class="brand-dot"></span>Bright Path</div>
    <div class="url">www.brightpath-example.test</div>
  </div>
  <h1 class="abs headline">NEED A DOCTOR?</h1>
  <p class="abs lead">Use this Bright Path card has the NFC Access Card for who’s need the real doctors providing real care without the waiting room.</p>
  <div class="abs steps-panel"></div>
  <div class="abs book-pill">How to Book an Appointment<br>using your Bright Path Card</div>
  <div class="abs tap-illustration" role="img" aria-label="Hand tapping the Bright Path card on a phone held in the other hand"></div>

  <div class="abs step" style="top:464px">
    <h3><span class="radio"></span>Step 1: Tap Your Card on Your Phone</h3>
    <ul><li>Hold your card near the back of your phone.</li><li>It will activate automatically — no app needed.</li><li>The Bright Path scheduler will open.</li></ul>
  </div>
  <div class="abs step" style="top:540px">
    <h3><span class="radio"></span>Step 2: Schedule Your Appointment</h3>
    <ul><li>Select your clinical concern.</li><li>Choose your time window.</li><li>Register (only once).</li><li>Confirm your appointment.</li></ul>
  </div>
  <div class="abs step" style="top:628px">
    <h3><span class="radio"></span>Step 3: Relax, we’ll take care of the rest</h3>
    <ul><li>A doctor will call during your scheduled time.</li><li>Once booked, you’ll be able to call our office.</li><li>No emails, no texts — just a real person.</li><li>It’s that simple</li></ul>
  </div>
</section>

<section class="sheet sheet--back">
  <header class="abs masthead"><span class="brand-dot"></span>Bright Path</header>

  <div class="abs panel about"></div>
  <div class="abs label" style="left:76px;top:117px;width:105px">ABOUT US</div>
  <div class="abs about-copy">
    <p>Bright Path was founded by Dr. Marcus Ferrigan, a Canadiantrained physician, to bring efficiency and convenience back into everyday healthcare.</p>
    <p><strong>Our mission is clear: provide convenient care for common concerns.</strong></p>
    <p>Instead of spending hours in crowded walk-in clinics or the emergency department, patients can book a visit, go about their day, and connect with a doctor when it’s their turn. No wasted time, no unnecessary hassle. For physicians, Bright Path creates a streamlined way to deliver timely, high-quality care — allowing them to focus on patients while reducing system strain. With Bright Path, healthcare fits into your life — not the other way around.</p>
  </div>

  <div class="abs panel services"></div>
  <div class="abs label" style="left:286px;top:117px;width:140px">OUR SERVICES</div>
  <p class="abs services-copy">Our doctors can address 120+ health concerns virtually — providing quality care without the waiting room.</p>
  <p class="abs service-list">Medical Documentation, Ent (Ear, Nose &amp; Throat), Woman’s &amp; Men’s Health Assessment, Skin Concerns, Mental Health, Preventative Health, Sexual Health, Common Infections, Joint &amp; Muscle Pain (Msk), Gastrointestinal Symptoms, Simple Visits; Medical notes, Sick notes, and so much more.</p>

  <div class="abs panel why"></div>
  <div class="abs label" style="left:94px;top:438px;width:292px;line-height:24px">WHY PATIENTS CHOOSE BRIGHT PATH</div>
  <div class="abs why-item" style="left:33px;width:124px"><h4><span class="radio"></span>Easy access</h4><p>Book and be seen from anywhere in BC.</p></div>
  <div class="abs why-item" style="left:159px;width:130px"><h4><span class="radio"></span>Effortless booking</h4><p>Tap your Bright Path card to begin.</p></div>
  <div class="abs why-item" style="left:300px;width:160px"><h4><span class="radio"></span>Trusted physicians</h4><p>Every visit is with a licensed BC family doctor.</p></div>

  <div class="abs panel visit"></div>
  <div class="abs label" style="left:146px;top:546px;width:192px;line-height:23px">HOW YOUR VISIT WORK</div>
  <div class="abs visit-step" style="left:35px"><div class="num">1</div><h4>Choose Your Time<br>Window</h4><p>The doctor offers set time windows for appointments—like 2:00 – 4:00 PM—and you pick the one that works best for you.</p></div>
  <div class="abs visit-step" style="left:148px;width:88px"><div class="num">2</div><h4>Get Your Spot<br>in Line</h4><p>Patients in your window are seen in the order they booked just like taking a ticket.</p></div>
  <div class="abs visit-step" style="left:252px;width:90px"><div class="num">3</div><h4>We’ll Notify You<br>When It’s Your Turn</h4><p>You’ll get messages as your turn gets closer.</p></div>
  <div class="abs visit-step" style="left:369px;top:581px;width:84px"><div class="num">4</div><h4>The Doctor Will<br>Call You</h4><p>When it’s your turn, the doctor will call you to start your virtual visit</p></div>

  <footer class="abs footer-band">Convenient Care For Common Concerns.</footer>
</section>

</body>
</html>
```